Plakat-Design für Vogelvolieren
Zielgruppe
Es geht um vier Din A4-Plakate, die an vier Vogelvolieren hängen und Informationen zu den Vögeln bieten, die sich in den Volieren befinden.
Die Volieren gehören zum Tierpark Haselbrück. Einem kleinen Wildpark, bei dem ausschließlich Ehrenamtliche tätig sind. Der Eintritt ist frei.
Die Zielgruppe sind die Besucher - von klein bis groß, von jung bis alt
Aufgabenstellung
Gute Lesbarkeit, denn die Informationsvermittlung soll im Vordergrund stehen.
Wir benötigen 1 Plakatdesign und die offenen Daten in InDesign, denn dann würden wir bei den weiteren drei Plakaten die Texte und Fotos austauschen.
Es sind 2 Plakate mit 4 Vögeln und 2 Plakate mit 2 Vögeln.

```html
<!DOCTYPE html>
<html lang="de">
<head>
<meta charset="utf-8">
<title>Volieren-Plakate – Tierpark Haselbrück</title>
<link rel="stylesheet" href="https://fonts.googleapis.com/css2?family=Alegreya:wght@500;700&family=Fira+Sans+Extra+Condensed:wght@400;500&display=swap">
<style>
:root{
  --backdrop:#a3a3a3;
  --paper:#f4f4f2;
  --purple:#8a2466;
  --green:#5d9e4f;
  --green-text:#5aa04a;
  --orange:#d49a3e;
  --ink:#1f1f1f;
  --red:#c0282c;
}
*{box-sizing:border-box;margin:0;padding:0}
html,body{width:1200px;height:2400px;overflow:hidden;background:var(--backdrop)}
body{position:relative;font-family:"Fira Sans Extra Condensed",sans-serif;color:var(--ink)}
.poster{position:absolute;left:231px;width:732px;height:1032px;background:var(--paper)}
.poster--four{top:79px}
.poster--two{top:1281px}
.cell{position:absolute;width:366px;background:var(--paper);overflow:hidden}
.cell--tl{left:0;top:0}
.cell--tr{left:366px;top:0}
.cell--bl{left:0;top:517px}
.cell--br{left:366px;top:517px}
.poster--four .cell{height:515px}
.poster--two .cell{height:611px}
.divider-v{position:absolute;left:364px;top:0;width:3px;background:var(--green)}
.poster--four .divider-v{height:1032px}
.poster--two .divider-v{height:611px}
.divider-h{position:absolute;left:0;top:514px;width:732px;height:3px;background:var(--green)}
.photo{position:absolute;left:0;top:0;width:366px;height:280px}
.photo--lovebirds{background:linear-gradient(160deg,#c99a5a,#a8793e 55%,#7fae5e)}
.photo--zebrafinch{background:linear-gradient(150deg,#c9aa72,#d8c49a 50%,#8d8378)}
.photo--quail{background:linear-gradient(170deg,#c9b497,#8d7a63 55%,#b59c77)}
.photo--cockatiel{background:linear-gradient(160deg,#6e5a48,#b2b2a8 55%,#d8cf8f)}
.photo--greyparrot{background:linear-gradient(150deg,#d9b684,#9a9a9a 50%,#b36d3e)}
.photo--jpquail{background:linear-gradient(160deg,#cfcbc4,#b9a78c 55%,#e2ddd4)}
.waves{position:absolute;left:0;top:0;width:366px;height:290px}
.brand{position:absolute;right:12px;top:12px;display:flex;align-items:center;gap:5px;font-size:10px;font-weight:500;color:var(--purple);width:84px;line-height:1.1}
.brand__dot{width:12px;height:12px;border-radius:50%;background:var(--purple);flex:none}
.title{position:absolute;background:var(--purple);color:#fff;font-family:"Alegreya",serif;font-weight:500;font-size:20px;line-height:1.15;text-align:center;display:flex;align-items:center;justify-content:center;border-radius:22px 30px 18px 26px;padding:4px 10px}
.col{position:absolute;text-align:center;font-size:11px;line-height:15px}
.col p+p{margin-top:7px}
.col--main{left:12px;top:266px;width:192px}
.col--range{left:214px;top:317px;width:142px}
.heading{font-size:14px;font-weight:500;color:var(--purple);text-decoration:underline;margin-bottom:8px}
.fact{color:var(--green-text)}
.map{width:90px;height:52px;margin:0 auto 12px;border-radius:6px;background:linear-gradient(90deg,#6aa55b,#5d9e4f);}
.wide-fact{position:absolute;left:0;width:366px;text-align:center;font-size:11px;color:var(--green-text);top:492px}
.notice{position:absolute;left:0;top:660px;width:732px;height:140px}
.notice__sign{position:absolute;left:154px;top:11px;width:112px;height:112px}
.notice__head{position:absolute;left:285px;top:20px;font-family:"Alegreya",serif;font-weight:700;font-size:42px;color:var(--red);line-height:1}
.notice__text{position:absolute;left:285px;top:74px;font-size:20px;font-weight:500;line-height:30px;color:var(--ink)}
</style>
</head>
<body>

<section class="poster poster--four">
  <article class="cell cell--tl">
    <div class="photo photo--lovebirds" role="img" aria-label="Foto: Unzertrennliche auf einem Ast in der Voliere"></div>
    <svg class="waves" viewBox="0 0 366 290" preserveAspectRatio="none" aria-hidden="true">
      <path d="M240 0 C262 24 290 44 366 54 L366 0Z" fill="var(--orange)"/>
      <path d="M254 0 C278 20 300 36 366 44 L366 0Z" fill="var(--paper)"/>
      <path d="M0 290 L0 258 C50 232 110 232 170 252 C240 276 300 272 366 246 L366 290Z" fill="var(--orange)"/>
      <path d="M0 290 L0 272 C70 250 120 254 180 268 C240 282 300 280 366 260 L366 290Z" fill="var(--green)"/>
      <path d="M0 290 L0 280 C70 262 120 264 180 276 C240 288 300 288 366 270 L366 290Z" fill="var(--paper)"/>
    </svg>
    <div class="brand"><span class="brand__dot"></span>Tierpark Haselbrück</div>
    <h2 class="title" style="left:9px;top:191px;width:172px;height:36px">Unzertrennliche</h2>
    <div class="col col--main">
      <h3 class="heading">Aussehen:</h3>
      <p>Ihre Farbgebung gibt den verschiedenen Arten ihren Namen. Es gibt Grauköpfchen, Orangeköpfchen, Tarantapapageien, Grünköpfchen, Rosenköpfchen, Pfirsichköpfchen, Schwarzköpfchen, Erdbeerköpfchen und Rußköpfchen.</p>
      <p>Unzertrennliche werden rund 13 bis 18 Zentimeter lang und wiegen etwa 50 Gramm.</p>
      <p class="fact">Wussten Sie, das Unzertrennliche im Englischen „Lovebirds“ (übersetzt: „Liebesvögel“) heißen?</p>
    </div>
    <div class="col col--range">
      <h3 class="heading">Vorkommen:</h3>
      <div class="map" role="img" aria-label="Weltkarte mit markiertem Verbreitungsgebiet in Afrika"></div>
      <p>Unzertrennliche leben in Afrika sowohl in heißen Savannen als auch in feucht-tropischen Regenwäldern.</p>
    </div>
  </article>

  <article class="cell cell--tr">
    <div class="photo photo--zebrafinch" role="img" aria-label="Foto: Zebrafink auf einem Zweig"></div>
    <svg class="waves" viewBox="0 0 366 290" preserveAspectRatio="none" aria-hidden="true">
      <path d="M240 0 C262 24 290 44 366 54 L366 0Z" fill="var(--orange)"/>
      <path d="M254 0 C278 20 300 36 366 44 L366 0Z" fill="var(--paper)"/>
      <path d="M0 290 L0 258 C50 232 110 232 170 252 C240 276 300 272 366 246 L366 290Z" fill="var(--orange)"/>
      <path d="M0 290 L0 272 C70 250 120 254 180 268 C240 282 300 280 366 260 L366 290Z" fill="var(--green)"/>
      <path d="M0 290 L0 280 C70 262 120 264 180 276 C240 288 300 288 366 270 L366 290Z" fill="var(--paper)"/>
    </svg>
    <div class="brand"><span class="brand__dot"></span>Tierpark Haselbrück</div>
    <h2 class="title" style="left:216px;top:180px;width:140px;height:70px">Australische Zebrafinken</h2>
    <div class="col col--main">
      <h3 class="heading">Aussehen:</h3>
      <p>Gut zu erkennen sind Zebrafinken an ihrem orange-roten Schnabel, am schwarzen Tränenstrich unter den Augen und der schwarzen Zebra-Musterung der Brust. Das Gefieder der Männchen, die über einen orange-farbenen Wangenfleck verfügen, ist kräftiger als das der Weibchen. Ihre kurzen, eckigen Flügel machen Zebrafinken zu wahren Flugakrobaten.</p>
      <p>Zebrafinken werden rund 12 Zentimeter lang und wiegen 12 bis 14 Gramm.</p>
    </div>
    <div class="col col--range">
      <h3 class="heading">Vorkommen:</h3>
      <div class="map" role="img" aria-label="Weltkarte mit markiertem Verbreitungsgebiet in Australien"></div>
      <p>Australische Zebrafinken leben fast überall in Australien.</p>
      <p class="fact">Lorem ipsum dolor sit amet, consetetur sadipscing elitr, sed diam</p>
    </div>
  </article>

  <article class="cell cell--bl">
    <div class="photo photo--quail" role="img" aria-label="Foto: Europäische Wachtel auf Sandboden"></div>
    <svg class="waves" viewBox="0 0 366 290" preserveAspectRatio="none" aria-hidden="true">
      <path d="M240 0 C262 24 290 44 366 54 L366 0Z" fill="var(--orange)"/>
      <path d="M254 0 C278 20 300 36 366 44 L366 0Z" fill="var(--paper)"/>
      <path d="M0 290 L0 258 C50 232 110 232 170 252 C240 276 300 272 366 246 L366 290Z" fill="var(--orange)"/>
      <path d="M0 290 L0 272 C70 250 120 254 180 268 C240 282 300 280 366 260 L366 290Z" fill="var(--green)"/>
      <path d="M0 290 L0 280 C70 262 120 264 180 276 C240 288 300 288 366 270 L366 290Z" fill="var(--paper)"/>
    </svg>
    <div class="brand"><span class="brand__dot"></span>Tierpark Haselbrück</div>
    <h2 class="title" style="left:200px;top:175px;width:152px;height:72px">Europäische Wachteln</h2>
    <div class="col col--main">
      <h3 class="heading">Aussehen:</h3>
      <p>Europäische Wachteln, die auch als Feldwachteln bezeichnet werden, haben eine graubraune Gesamtfärbung mit einer Vielzahl rotbrauner und schwarzer Striche. Die Flügel sind grau. Die Augenfarbe ist rotbraun und damit ein Unterscheidungsmerkmal, denn die japanischen Zuchtwachteln haben dunkle Augen.</p>
      <p>Wachteln wiegen rund 90 bis 100 Gramm.</p>
    </div>
    <div class="col col--range">
      <h3 class="heading">Vorkommen:</h3>
      <div class="map" role="img" aria-label="Weltkarte mit markiertem Verbreitungsgebiet in Europa, Asien und Afrika"></div>
      <p>Europäische Wachteln leben in fast ganz Europa, den westlichen Teil Asiens und einem großen Teil Afrikas.</p>
    </div>
    <p class="wide-fact">Lorem ipsum dolor sit amet, consetetur sadipscing elitr, sed diam rebum.</p>
  </article>

  <article class="cell cell--br">
    <div class="photo photo--cockatiel" role="img" aria-label="Foto: Nymphensittich auf einer Sitzstange vor dem Volierengitter"></div>
    <svg class="waves" viewBox="0 0 366 290" preserveAspectRatio="none" aria-hidden="true">
      <path d="M240 0 C262 24 290 44 366 54 L366 0Z" fill="var(--orange)"/>
      <path d="M254 0 C278 20 300 36 366 44 L366 0Z" fill="var(--paper)"/>
      <path d="M0 290 L0 258 C50 232 110 232 170 252 C240 276 300 272 366 246 L366 290Z" fill="var(--orange)"/>
      <path d="M0 290 L0 272 C70 250 120 254 180 268 C240 282 300 280 366 260 L366 290Z" fill="var(--green)"/>
      <path d="M0 290 L0 280 C70 262 120 264 180 276 C240 288 300 288 366 270 L366 290Z" fill="var(--paper)"/>
    </svg>
    <div class="brand"><span class="brand__dot"></span>Tierpark Haselbrück</div>
    <h2 class="title" style="left:0;top:18px;width:184px;height:50px;border-radius:0 30px 22px 0">Katharinasittiche</h2>
    <div class="col col--main">
      <h3 class="heading">Aussehen:</h3>
      <p>Mit ihrem leuchtend grünen Gefieder mit blauschwarzen Abzeichen sind Katharinasittiche perfekt an die Wälder in ihrer Heimat angepasst. Aufgrund von gezielten Züchtungen gibt es mittlerweile auch gelbe, blaue, türkis- und creme-farbene Katharinasittiche. Männliche und weibliche Katharinasittiche lassen sich äußerlich kaum unterscheiden.</p>
      <p>Erwachsene Vögel werden 16 bis 17 Zentimeter lang, wobei der Schwanz rund 6 Zentimeter misst, und wiegen etwa 50 bis 60 Gramm.</p>
    </div>
    <div class="col col--range">
      <h3 class="heading">Vorkommen:</h3>
      <div class="map" role="img" aria-label="Weltkarte mit markiertem Verbreitungsgebiet in Mittel- und Südamerika"></div>
      <p>Katharinasittiche leben in Mittel- und Südamerika.</p>
      <p class="fact">Lorem ipsum dolor sit amet, consetetur sadipscing elitr, sed diam nonumy eirmod tempor</p>
    </div>
  </article>

  <div class="divider-v"></div>
  <div class="divider-h"></div>
</section>

<section class="poster poster--two">
  <article class="cell cell--tl">
    <div class="photo photo--greyparrot" role="img" aria-label="Foto: Graupapagei auf einer Sitzstange"></div>
    <svg class="waves" viewBox="0 0 366 290" preserveAspectRatio="none" aria-hidden="true">
      <path d="M240 0 C262 24 290 44 366 54 L366 0Z" fill="var(--orange)"/>
      <path d="M254 0 C278 20 300 36 366 44 L366 0Z" fill="var(--paper)"/>
      <path d="M0 290 L0 258 C50 232 110 232 170 252 C240 276 300 272 366 246 L366 290Z" fill="var(--orange)"/>
      <path d="M0 290 L0 272 C70 250 120 254 180 268 C240 282 300 280 366 260 L366 290Z" fill="var(--green)"/>
      <path d="M0 290 L0 280 C70 262 120 264 180 276 C240 288 300 288 366 270 L366 290Z" fill="var(--paper)"/>
    </svg>
    <div class="brand"><span class="brand__dot"></span>Tierpark Haselbrück</div>
    <h2 class="title" style="left:190px;top:187px;width:161px;height:75px">Kongo-Graupapageien</h2>
    <div class="col col--main">
      <h3 class="heading">Aussehen:</h3>
      <p>Kongo-Graupapageien, die sehr intelligent und sprachbegabt sind, gehören mit einer Größe von über 30 Zentimetern zu den größten Papageien Afrikas und werden rund 450 Gramm schwer. Seinen Namen verdankt der Graupapagei seinem überwiegend grauen Gefieder. Auffallend ist ihre sehr helle Gesichtspartie. Im Gegensatz zu Timneh-Graupapageien haben Kongo-Graupapageien leuchtend hellrote Schwanzfedern.</p>
      <p class="fact">Wussten Sie, dass Graupapageien 50 bis 80 Jahre alt werden können?</p>
    </div>
    <div class="col col--range">
      <h3 class="heading">Vorkommen:</h3>
      <div class="map" role="img" aria-label="Weltkarte mit markiertem Verbreitungsgebiet in Zentralafrika"></div>
      <p>Die Heimat von Kongo-Graupapageien liegt in Zentralafrika. Genauer gesagt findet man diese geselligen Vögel im Kongo, in Gabun sowie in Teilen von Nigeria, Kamerun, Kenia und Tansania. Kongo-Graupapageien, die typische Baumbewohner sind, fühlen sich in tropischen Regenwäldern, Mangroven und Feuchtsavannen wohl.</p>
    </div>
  </article>

  <article class="cell cell--tr">
    <div class="photo photo--jpquail" role="img" aria-label="Foto: Japanische Legewachtel auf hellem Sand"></div>
    <svg class="waves" viewBox="0 0 366 290" preserveAspectRatio="none" aria-hidden="true">
      <path d="M240 0 C262 24 290 44 366 54 L366 0Z" fill="var(--orange)"/>
      <path d="M254 0 C278 20 300 36 366 44 L366 0Z" fill="var(--paper)"/>
      <path d="M0 290 L0 258 C50 232 110 232 170 252 C240 276 300 272 366 246 L366 290Z" fill="var(--orange)"/>
      <path d="M0 290 L0 272 C70 250 120 254 180 268 C240 282 300 280 366 260 L366 290Z" fill="var(--green)"/>
      <path d="M0 290 L0 280 C70 262 120 264 180 276 C240 288 300 288 366 270 L366 290Z" fill="var(--paper)"/>
    </svg>
    <div class="brand"><span class="brand__dot"></span>Tierpark Haselbrück</div>
    <h2 class="title" style="left:219px;top:181px;width:142px;height:72px">Japanische Legewachteln</h2>
    <div class="col col--main">
      <h3 class="heading">Aussehen:</h3>
      <p>Japanische Legewachteln, die sehr zutraulich werden können, gibt es in vielfältigen Farbschlägen, wie die Fell-, Haut- und Federfärbung bei verschiedenen Tieren genannt wird. Anerkannte Farbschläge sind unter anderem wildfarbig, gelb-, braun- und silber-wildfarbig sowie weiß. Japanischen Legewachteln gemein ist, dass ihr Körper sehr gedrungen wirkt. Ausgewachsene Legewachteln wiegen in der Regel rund 250 bis 300 Gramm, wobei die Hähne meist etwas kleiner, schlanker und leichter sind als Hennen.</p>
      <p class="fact">Wussten Sie, dass Wachteln sehr gut fliegen können, obwohl sie das fast ausschließlich in Gefahrensituationen tun? Sie können sogar wie ein Helikopter senkrecht nach oben aufsteigen.</p>
    </div>
    <div class="col col--range">
      <h3 class="heading">Vorkommen:</h3>
      <div class="map" role="img" aria-label="Weltkarte mit markiertem Verbreitungsgebiet in Ostasien"></div>
      <p>Wie der Name schon vermuten lässt, ist Japan die ursprüngliche Heimat von Japanischen Legewachteln. Auch in Korea und in Teilen Chinas war die Wildform der Legewachtel schon früh zu finden. Seit dem 13. Jahrhundert werden die Legewachteln in Japan als Ziervogel gehalten.</p>
    </div>
  </article>

  <div class="divider-v"></div>

  <aside class="notice">
    <svg class="notice__sign" viewBox="0 0 112 112" aria-hidden="true">
      <circle cx="56" cy="56" r="50" fill="#eeeeee"/>
      <circle cx="56" cy="56" r="44" fill="#d9d9d9"/>
      <path d="M24 22 L90 88" stroke="var(--red)" stroke-width="10"/>
      <circle cx="56" cy="56" r="50" fill="none" stroke="var(--red)" stroke-width="11"/>
      <circle cx="56" cy="56" r="55" fill="none" stroke="#222" stroke-width="1.5"/>
    </svg>
    <h2 class="notice__head">Achtung!</h2>
    <p class="notice__text">Keine Finger in die Voliere stecken –<br>Graupapageien können beißen.</p>
  </aside>
</section>

</body>
</html>
```